THE HEADLAND AT TALL PINE HUDSON RIVER WATERFRONT LAND

crisp clear business cards on wood stock or thick paper with large font with a river otter logo, PERSONAL INFO ON ONE SIDE, PROJECT INFO ON THE OTHER SIDE
Updates

I don’t have a logo. Just thought that a photo of a river otter would look appealing.

Target Market(s)

Buyers and realtors

Industry/Entity Type

Real Estate Development

Contact Information for Business Card

MARTIN KOWALCZYK
607-318-5942 (Call or Text)
STONE MEADOW LLC PRINCIPAL

RQVWFIELD@NORVAMAIL.NET

Font styles to use
Sans Serif

Colors
fbfdfe
0792cd
00a990
fbed22
ec1f27

Requirements
Must have
• LARGE FONT, ROUNDED EDGES,
Nice to have
• ON THE BACK SIDE :
• THE HEADLAND AT TALL PINE
• HUDSON RIVER WATERFRONT LAND
• 2 TO 67 ACRES---READY TO BUILD
• PRICED TO SELL!

```html
<!DOCTYPE html>
<html lang="en">
<head>
<meta charset="utf-8">
<title>Stone Meadow LLC — Business Card</title>
<link rel="stylesheet" href="https://fonts.googleapis.com/css2?family=Montserrat:wght@400;600;700;800&display=swap">
<style>
  :root {
    --backdrop: #000000;
    --ink: #1b1a17;
    --wood-light: #e6cc9c;
    --wood-mid: #c9a570;
    --wood-dark: #a57d4c;
    --wood-glow: #f3e2b8;
  }
  * { box-sizing: border-box; margin: 0; padding: 0; }
  html, body { width: 1200px; height: 1000px; overflow: hidden; background: var(--backdrop); }
  body { position: relative; font-family: "Montserrat", sans-serif; color: var(--ink); }

  .card {
    position: absolute;
    left: 260px;
    width: 681px;
    height: 388px;
    border-radius: 42px;
    overflow: hidden;
  }
  .card--front { top: 90px; }
  .card--back { top: 526px; }

  .wood {
    position: absolute;
    inset: 0;
    background:
      radial-gradient(ellipse 55% 55% at 50% 45%, var(--wood-glow) 0%, rgba(243,226,184,0) 70%),
      repeating-linear-gradient(178deg, rgba(165,125,76,0) 0 18px, rgba(165,125,76,0.35) 18px 22px, rgba(165,125,76,0) 22px 34px),
      linear-gradient(90deg, var(--wood-dark) 0%, var(--wood-mid) 25%, var(--wood-light) 50%, var(--wood-mid) 75%, var(--wood-dark) 100%);
  }

  /* Front: brand block */
  .brand {
    position: absolute;
    left: 0; right: 0;
    top: 95px;
    display: flex;
    flex-direction: column;
    align-items: center;
  }
  .brand__mark {
    width: 122px;
    height: 122px;
    background: var(--ink);
  }
  .brand__name {
    margin-top: 18px;
    font-weight: 800;
    font-size: 40px;
    letter-spacing: 0.5px;
    line-height: 1;
    text-align: center;
  }

  /* Back: contact */
  .contact {
    position: absolute;
    right: 364px;
    top: 142px;
    text-align: right;
    white-space: nowrap;
  }
  .contact__name { font-size: 27px; line-height: 1; font-weight: 400; }
  .contact__name strong { font-weight: 800; }
  .contact__role { margin-top: 8px; font-size: 17px; font-weight: 700; letter-spacing: 1px; }
  .contact__phone { margin-top: 16px; font-size: 17px; font-weight: 700; }
  .contact__phone span { font-size: 15px; }
  .contact__email { margin-top: 9px; font-size: 17px; font-weight: 700; }

  .divider {
    position: absolute;
    left: 334px;
    top: 131px;
    width: 3px;
    height: 142px;
    background: var(--ink);
  }

  .project {
    position: absolute;
    left: 352px;
    top: 145px;
    list-style: none;
  }
  .project__item {
    display: flex;
    align-items: center;
    height: 31px;
    font-size: 13.5px;
    font-weight: 800;
    white-space: nowrap;
  }
  .project__item::before {
    content: "";
    width: 11px;
    height: 11px;
    margin-right: 7px;
    background: var(--ink);
  }
</style>
</head>
<body>
  <section class="card card--front">
    <div class="wood" role="img" aria-label="Light wood grain texture"></div>
    <div class="brand">
      <div class="brand__mark"></div>
      <p class="brand__name">STONE MEADOW LLC</p>
    </div>
  </section>

  <section class="card card--back">
    <div class="wood" role="img" aria-label="Light wood grain texture"></div>
    <div class="contact">
      <p class="contact__name">MARTIN <strong>KOWALCZYK</strong></p>
      <p class="contact__role">PRINCIPAL</p>
      <p class="contact__phone">607-318-5942 <span>(Call or Text)</span></p>
      <p class="contact__email">RQVWFIELD@NORVAMAIL.NET</p>
    </div>
    <div class="divider"></div>
    <ul class="project">
      <li class="project__item">THE HEADLAND AT TALL PINE</li>
      <li class="project__item">HUDSON RIVER WATERFRONT LAND</li>
      <li class="project__item">2 TO 67 ACRES - READY TO BUILD</li>
      <li class="project__item">PRICED TO SELL!</li>
    </ul>
  </section>
</body>
</html>
```